business card for a massage therapy practice named 'Meadow and Rowan Massage Studio'

I really need a trendy, yet easy on the eyes business card to complement my logo. Ideally with some gold or rose gold foil work.

My uploaded file of the logo I have in horizontal but I have a vertical version as well. Another color that is used in the website is a blush pink here and there. I'd like to see some trendy tropical leaves in the design.

```html
<!DOCTYPE html>
<html lang="en">
<head>
<meta charset="utf-8">
<title>Meadow &amp; Rowan Massage Studio – Business Card</title>
<link rel="stylesheet" href="https://fonts.googleapis.com/css2?family=Open+Sans:wght@400;600&display=swap">
<style>
  :root {
    --canvas: #ffffff;
    --blush: #fcc0c7;
    --leaf-light: #a9c47f;
    --leaf-mid: #8fa46a;
    --leaf-dark: #6e6266;
    --ink: #231f20;
    --gold: #a48d5f;
    --label: #f6c9c9;
    --label-edge: #4a3f42;
  }
  * { margin: 0; padding: 0; box-sizing: border-box; }
  html, body {
    width: 1034px; height: 1200px; overflow: hidden;
    background: var(--canvas);
    font-family: "Open Sans", Arial, sans-serif;
  }
  .card {
    position: absolute; left: 44px;
    width: 947px; height: 570px; overflow: hidden;
  }
  .card--front { top: 19px; }
  .card--back { top: 618px; }
  .card__foliage { position: absolute; inset: 0; width: 100%; height: 100%; }
  .brand {
    position: absolute; display: flex; align-items: center; gap: 18px;
    color: var(--ink); font-weight: 600; line-height: 1.1;
  }
  .brand__dot { border-radius: 50%; background: var(--gold); flex: none; }
  .card--front .brand { left: 340px; top: 140px; font-size: 40px; }
  .card--front .brand__dot { width: 64px; height: 64px; }
  .card--back .brand { left: 190px; top: 205px; font-size: 54px; }
  .card--back .brand__dot { width: 88px; height: 88px; }
  .brand__tagline { display: block; font-size: 0.62em; letter-spacing: 0.18em; text-transform: uppercase; }
  .outlined {
    position: absolute; color: var(--label);
    text-shadow: -1px -1px 0 var(--label-edge), 1px -1px 0 var(--label-edge),
                 -1px 1px 0 var(--label-edge), 1px 1px 0 var(--label-edge);
  }
  .holder__name { left: 188px; top: 325px; font-size: 36px; }
  .holder__role { left: 188px; top: 391px; font-size: 19px; }
  .contact { position: absolute; right: 133px; top: 320px; text-align: right; font-size: 19px; }
  .contact .outlined { position: static; display: block; margin-bottom: 12px; }
  .back__web {
    position: absolute; left: 0; right: 0; top: 510px; text-align: center;
    font-size: 18px; color: #ffffff;
    text-shadow: 0 0 2px var(--ink), 1px 1px 1px var(--ink);
  }
</style>
</head>
<body>

<section class="card card--front">
  <svg class="card__foliage" viewBox="0 0 947 570" role="img" aria-label="Frame of tropical palm and banana leaves around a blush pink centre">
    <defs>
      <linearGradient id="leafFront" x1="0" y1="0" x2="1" y2="1">
        <stop offset="0" stop-color="var(--leaf-light)"/>
        <stop offset="0.5" stop-color="var(--leaf-dark)"/>
        <stop offset="1" stop-color="var(--leaf-mid)"/>
      </linearGradient>
    </defs>
    <rect width="947" height="570" fill="url(#leafFront)"/>
    <path fill="var(--blush)" d="M150,130 C260,60 520,110 680,90 C800,70 860,140 800,230 C840,300 800,380 720,440 C600,500 420,470 300,480 C200,490 150,420 170,330 C120,260 110,180 150,130Z"/>
  </svg>
  <div class="brand">
    <span class="brand__dot"></span>
    <span>Meadow &amp; Rowan<span class="brand__tagline">Massage Studio</span></span>
  </div>
  <p class="outlined holder__name">NAME</p>
  <p class="outlined holder__role">PROFESSION</p>
  <div class="contact">
    <span class="outlined">008 412 735 2096</span>
    <span class="outlined">hello@meadowrowan.com</span>
    <span class="outlined">www.meadowrowan.com</span>
  </div>
</section>

<section class="card card--back">
  <svg class="card__foliage" viewBox="0 0 947 570" role="img" aria-label="Frame of tropical palm and banana leaves around a blush pink centre">
    <defs>
      <linearGradient id="leafBack" x1="0" y1="0" x2="1" y2="1">
        <stop offset="0" stop-color="var(--leaf-light)"/>
        <stop offset="0.5" stop-color="var(--leaf-dark)"/>
        <stop offset="1" stop-color="var(--leaf-mid)"/>
      </linearGradient>
    </defs>
    <rect width="947" height="570" fill="url(#leafBack)"/>
    <path fill="var(--blush)" d="M150,130 C260,60 520,110 680,90 C800,70 860,140 800,230 C840,300 800,380 720,440 C600,500 420,470 300,480 C200,490 150,420 170,330 C120,260 110,180 150,130Z"/>
  </svg>
  <div class="brand">
    <span class="brand__dot"></span>
    <span>Meadow &amp; Rowan<span class="brand__tagline">Massage Studio</span></span>
  </div>
  <p class="back__web">www.meadowrowan.com</p>
</section>

</body>
</html>
```